PLUM BUSINESS CARD

Need a business card and logo. The company name is PLUM (Piedmont League of Ultimate Mareriders). It's a business that offers horseback riding lessons to young girls. Please put my name: Renata Bowley and a place for email and phone number. I would like the card to look feminine and soft. I like script type lettering. I want the card to be white or ivory with black or gray and hot pink print. A horse head outline would be cool, something whimsical. Think teen girl who likes glamour. Also, I give western riding lessons. So I like faded out background Images of western saddles, cowgirls, horses with long hair, ropes, horses in sunset...mabe the word PLUM can be made out of a lasso rope?

Just updated my project with a little more detail

Target Market(s)

Young girls/ cowgirls, western riding

Industry/Entity Type

Horseback Riding

Font styles to use
Script

Colors
e34197

Requirements
Must have
• A logo of PLUM.
Must say Piedmont League of Ultimate Mareriders
Colors are Pink and Black with an elegant, glamorous, feminine look.
Nice to have
• Could have a picture or outline of a horse

```html
<!DOCTYPE html>
<html lang="en">
<head>
<meta charset="utf-8">
<title>PLUM – Business Card Concepts</title>
<link href="https://fonts.googleapis.com/css2?family=Pinyon+Script&display=swap" rel="stylesheet">
<style>
  :root{
    --sheet:#ffffff;
    --card:#fafcc4;
    --frame:#ff4f9c;
    --pink:#f0459a;
    --hot:#ff1493;
    --soft:#ff5fa8;
    --ink:#111111;
    --faint:rgba(250,205,150,.35);
  }
  *{box-sizing:border-box;margin:0;padding:0}
  html,body{width:1200px;height:1000px;overflow:hidden;background:var(--sheet)}
  body{position:relative;font-family:"Pinyon Script",cursive;color:var(--pink)}
  .option-number{position:absolute;font-size:38px;color:var(--ink);line-height:1}
  .card{position:absolute;width:523px;height:319px;background:var(--card);border:4px solid var(--frame);border-radius:26px;overflow:hidden}
  .card > *{position:absolute}
  .backdrop{left:80px;top:10px;width:330px;height:300px;border-radius:50%;background:var(--faint)}
  .mark-dot{width:58px;height:58px;border-radius:50%;background:var(--hot)}
  .brand{font-size:58px;line-height:1;color:var(--pink);white-space:nowrap}
  .league{font-size:21px;line-height:1;color:var(--pink);white-space:nowrap;width:100%;text-align:center}
  .holder{font-size:30px;line-height:1;color:var(--hot);white-space:nowrap}
  .contact{font-size:14px;line-height:1;color:var(--hot);white-space:nowrap;display:flex;align-items:center;gap:6px}
  .contact svg{width:11px;height:11px;flex:none}
  .contact.right{right:36px;justify-content:flex-end}
  .swoosh{left:0;top:0;width:523px;height:319px}
  .logo{position:absolute;display:flex;flex-direction:column;align-items:center;gap:14px}
  .logo .mark-dot{width:70px;height:70px}
  .logo .brand{font-size:60px;color:var(--hot)}
</style>
</head>
<body>

  <!-- Card concept 1 -->
  <span class="option-number" style="left:148px;top:36px">1</span>
  <section class="card" style="left:195px;top:2px">
    <div class="backdrop" role="img" aria-label="Faint decorative emblem in the background"></div>
    <div class="mark-dot" style="left:232px;top:48px"></div>
    <div class="brand" style="left:0;width:100%;text-align:center;top:140px">PLUM</div>
    <div class="league" style="left:0;top:205px">Piedmont League of Ultimate Mareriders</div>
    <div class="holder" style="left:38px;top:262px">Renata Bowley</div>
    <div class="contact right" style="top:259px">041 327 5086
      <svg viewBox="0 0 11 11"><rect x="3" y="0.5" width="5" height="10" rx="1" fill="none" stroke="var(--hot)"/></svg></div>
    <div class="contact right" style="top:277px">plum@mailbox.com
      <svg viewBox="0 0 11 11"><rect x="0.5" y="2" width="10" height="7" fill="none" stroke="var(--hot)"/><path d="M0.5 2 L5.5 6 L10.5 2" fill="none" stroke="var(--hot)"/></svg></div>
  </section>

  <!-- Card concept 2 -->
  <span class="option-number" style="left:134px;top:357px">2</span>
  <section class="card" style="left:195px;top:333px">
    <div class="mark-dot" style="left:232px;top:48px"></div>
    <div class="brand" style="left:0;width:100%;text-align:center;top:140px">PLUM</div>
    <div class="league" style="left:0;top:205px">Piedmont League of Ultimate Mareriders</div>
    <div class="holder" style="left:38px;top:262px">Renata Bowley</div>
    <div class="contact right" style="top:259px">041 327 5086
      <svg viewBox="0 0 11 11"><rect x="3" y="0.5" width="5" height="10" rx="1" fill="none" stroke="var(--hot)"/></svg></div>
    <div class="contact right" style="top:277px">plum@mailbox.com
      <svg viewBox="0 0 11 11"><rect x="0.5" y="2" width="10" height="7" fill="none" stroke="var(--hot)"/><path d="M0.5 2 L5.5 6 L10.5 2" fill="none" stroke="var(--hot)"/></svg></div>
  </section>

  <!-- Card concept 3 -->
  <span class="option-number" style="left:126px;top:726px">3</span>
  <section class="card" style="left:193px;top:678px">
    <svg class="swoosh" viewBox="0 0 523 319" aria-hidden="true">
      <path d="M-5 136 Q 220 230 530 250" fill="none" stroke="var(--soft)" stroke-width="5"/>
      <path d="M-5 150 Q 220 242 530 262" fill="none" stroke="var(--hot)" stroke-width="5"/>
    </svg>
    <div class="mark-dot" style="left:130px;top:40px"></div>
    <div class="brand" style="left:208px;top:84px">PLUM</div>
    <div class="league" style="left:-10px;top:144px">Piedmont League of Ultimate Mareriders</div>
    <div class="holder" style="left:18px;top:222px">Renata Bowley</div>
    <div class="contact" style="left:18px;top:280px">
      <svg viewBox="0 0 11 11"><rect x="3" y="0.5" width="5" height="10" rx="1" fill="none" stroke="var(--hot)"/></svg>041 327 5086</div>
    <div class="contact right" style="top:280px">plum@mailbox.com
      <svg viewBox="0 0 11 11"><rect x="0.5" y="2" width="10" height="7" fill="none" stroke="var(--hot)"/><path d="M0.5 2 L5.5 6 L10.5 2" fill="none" stroke="var(--hot)"/></svg></div>
  </section>

  <!-- Logo concepts -->
  <div class="logo" style="left:855px;top:80px;width:140px">
    <div class="mark-dot"></div>
    <div class="brand">PLUM</div>
  </div>
  <span class="option-number" style="left:1052px;top:52px">1</span>

  <div class="logo" style="left:850px;top:440px;width:150px">
    <div class="mark-dot"></div>
    <div class="brand">PLUM</div>
  </div>
  <span class="option-number" style="left:1036px;top:422px">2</span>

  <div class="logo" style="left:855px;top:820px;width:140px">
    <div class="mark-dot"></div>
    <div class="brand">PLUM</div>
  </div>
  <span class="option-number" style="left:1030px;top:802px">3</span>

</body>
</html>
```